Business Card for Jewelry Business

We need a new namecard design for a jewelry company based in Bangkok, Thailand. We have a new website recently and want the new namecard to reflect our new modern image. I have uploaded our old namecard to show you the information that needs to be on the namecard. Pls check our website www.qelnotrax.com for the new color scheme to help design the new namecard.

```html
<!DOCTYPE html>
<html lang="en">
<head>
<meta charset="utf-8">
<title>Qelnotrax Business Card</title>
<link href="https://fonts.googleapis.com/css2?family=Libre+Baskerville:wght@400;700&display=swap" rel="stylesheet">
<style>
  :root {
    --backdrop: #3b3b3e;
    --card-black: #131313;
    --teal: #52c5cb;
    --ivory: #e6dfd6;
    --white: #ffffff;
    --text-light: #f2f2f2;
  }
  * { margin: 0; padding: 0; box-sizing: border-box; }
  html, body {
    width: 1200px; height: 801px; overflow: hidden;
    background: var(--backdrop);
    font-family: "Libre Baskerville", Georgia, serif;
  }
  .stage {
    position: relative; width: 1200px; height: 801px;
    display: flex; align-items: center; justify-content: center; gap: 32px;
  }
  .card {
    position: relative; width: 560px; height: 320px;
    border-radius: 16px; background: var(--card-black);
    overflow: hidden;
    box-shadow: 0 10px 28px rgba(0,0,0,.45);
  }
  /* Front */
  .brand {
    position: absolute; left: 0; right: 0; top: 0; bottom: 0;
    display: flex; align-items: center; justify-content: center; gap: 16px;
  }
  .brand-dot {
    width: 18px; height: 18px; border-radius: 50%; background: var(--teal);
  }
  .brand-name {
    color: var(--white); font-size: 34px; letter-spacing: 3px; font-weight: 400;
  }
  /* Back */
  .card-arc { position: absolute; inset: 0; width: 100%; height: 100%; }
  .back-brand {
    position: absolute; right: 40px; top: 96px;
    color: var(--teal); font-size: 20px; letter-spacing: 2px;
  }
  .details { position: absolute; left: 34px; top: 44px; color: var(--text-light); }
  .person-name {
    color: var(--teal); font-weight: 700; font-size: 22px; letter-spacing: 1px;
  }
  .person-title { font-size: 12.5px; margin-top: 6px; }
  .address { font-size: 12.5px; line-height: 1.55; margin-top: 26px; }
  .contacts { list-style: none; margin-top: 22px; font-size: 12.5px; }
  .contacts li { display: flex; align-items: center; gap: 10px; height: 20px; }
  .contacts svg { width: 13px; height: 13px; fill: var(--teal); flex: none; }
</style>
</head>
<body>
<main class="stage">
  <section class="card card-front">
    <div class="brand">
      <span class="brand-dot"></span>
      <span class="brand-name">QELNOTRAX</span>
    </div>
  </section>

  <section class="card card-back">
    <svg class="card-arc" viewBox="0 0 560 320" preserveAspectRatio="none" aria-hidden="true">
      <path d="M300 0 C300 170 410 300 560 322 L560 0 Z" fill="var(--teal)"/>
      <path d="M318 0 C320 150 420 258 560 282 L560 0 Z" fill="var(--white)"/>
    </svg>
    <div class="back-brand">QELNOTRAX</div>
    <div class="details">
      <h1 class="person-name">MINA SORAWAT</h1>
      <p class="person-title">Sales &amp; Product Development Manager</p>
      <p class="address">128 Moo 7 Rattanakorn Road,<br>Nong Chok Industrial Estate,<br>Bangkok, 10530 Thailand</p>
      <ul class="contacts">
        <li><svg viewBox="0 0 16 16"><path d="M3 1l3 3-1.5 2a9 9 0 0 0 5.5 5.5L12 10l3 3-2 2C7 15 1 9 1 3z"/></svg>+662-418-2257</li>
        <li><svg viewBox="0 0 16 16"><path d="M4 1h7v4H4zM2 6h12v9H2zm3 2v2h2V8zm4 0v2h2V8zm-4 3v2h2v-2zm4 0v2h2v-2z"/></svg>+662-581-3094</li>
        <li><svg viewBox="0 0 16 16"><path d="M1 3h14v10H1zm1 1.5V5l6 4 6-4v-.5z"/></svg>mina@qelnotrax.com</li>
        <li><svg viewBox="0 0 16 16"><path d="M8 1a7 7 0 1 0 0 14A7 7 0 0 0 8 1zm0 1.5c1 1.2 1.6 3 1.7 5H6.3c.1-2 .7-3.8 1.7-5zM2.6 8.5h2.2c.1 1.8.5 3.4 1.2 4.6a5.5 5.5 0 0 1-3.4-4.6z"/></svg>www.qelnotrax.com</li>
      </ul>
    </div>
  </section>
</main>
</body>
</html>
```